依頼詳細
今までの会社の名刺デザインはシンプルすぎるので刷新したいと思っています。念の為、現在使用している名刺のファイルを添付しております。会社のロゴマークはそのまま使用したいです。何卒宜しくお願い致します。
記載項目
表面:会社名/役職/名前/住所/電話/Fax/Mail
あと、名前に読み仮名用にローマ字も記載して頂きたいです。
希望イメージ
シンプル 複雑
単色 カラフル
暗い 明るい
日常 高級
遊び心 厳粛
未来的 伝統的
女性的 男性的
希望する色
お任せ致します。
納品ファイル
• 高解像度JPG (.jpg)
• イラストレーター形式 (.ai)
補足説明
前回、本サイトにて別会社のロゴマーク作成の依頼をした際に皆様のレベルがすごく高いのに驚きました。今回もどうか宜しくお願い致します。
依頼公開後の追記内容
ロゴマークの画像を掲載致しましたので宜しくお願い致します。

弊社にて社員の意見を聞いた結果で決定させて頂きました。とてもスッキリした綺麗なイメージが良かったです。

皆様、この度はご多用中にもかかわりませず、数多くのご提案をくださり、誠にありがたく厚く御礼申し上げます。
どれをとっても良いご提案ばかりで迷いましたが、最終は社員の意見を聞き、人気の高かった順より選定させて頂きました。
また今後も本サイトにて募集させて頂きますので、どうか今後とも宜しくお願い申し上げます。
本当にありがとうございました。

```html
<!DOCTYPE html>
<html lang="ja">
<head>
<meta charset="utf-8">
<title>株式会社青嶺建設 名刺デザイン Style C</title>
<link rel="stylesheet" href="https://fonts.googleapis.com/css2?family=Noto+Serif+JP:wght@500;700&family=Noto+Sans+JP:wght@400;500;700&family=Courier+Prime&display=swap">
<style>
  :root {
    --navy: #1e2a78;
    --navy-deep: #18206a;
    --orange: #e8841f;
    --ink: #111111;
    --skyline: #c9cbe6;
    --skyline-soft: #e9eaf6;
    --sheet: #ffffff;
    --label: #3a4a9a;
  }
  * { box-sizing: border-box; margin: 0; padding: 0; }
  html, body { width: 897px; height: 1200px; overflow: hidden; background: var(--sheet); }
  .sheet { position: relative; width: 897px; height: 1200px; font-family: "Noto Sans JP", sans-serif; }

  .card { position: absolute; background: #fff; border: 1.5px solid #9a9a9a; overflow: hidden; }
  .card--front { left: 59px; top: 111px; width: 366px; height: 674px; }
  .card--back { left: 469px; top: 433px; width: 381px; height: 695px; }

  .band { position: absolute; left: 0; right: 0; background: var(--navy);
    color: #fff; font-family: "Noto Serif JP", serif; font-weight: 700;
    display: flex; align-items: center; justify-content: center; }
  .band small { font-size: 0.62em; margin-right: 4px; }
  .card--front .band { top: 0; height: 66px; font-size: 26px; }
  .card--back .band { top: 0; height: 70px; font-size: 27px; }

  .brand { position: absolute; left: 0; right: 0; display: flex; align-items: center;
    justify-content: center; gap: 12px; color: var(--navy); font-weight: 700; letter-spacing: 2px; }
  .brand__dot { border-radius: 50%; background: var(--orange); }
  .card--front .brand { top: 118px; font-size: 34px; }
  .card--front .brand__dot { width: 30px; height: 30px; }
  .card--back .brand { top: 135px; font-size: 42px; }
  .card--back .brand__dot { width: 38px; height: 38px; }

  .services { position: absolute; left: 0; right: 0; top: 262px; text-align: center;
    color: var(--orange); font-size: 11.5px; font-family: "Noto Serif JP", serif; letter-spacing: 0.5px; }

  .name { position: absolute; left: 34px; top: 318px; font-family: "Noto Serif JP", serif;
    font-size: 58px; font-weight: 500; color: var(--ink); letter-spacing: 4px; }
  .role { position: absolute; left: 176px; top: 396px; font-family: "Noto Serif JP", serif;
    font-size: 27px; color: var(--ink); letter-spacing: 2px; }

  .skyline { position: absolute; left: 0; right: 0; }
  .card--front .skyline { top: 440px; height: 140px;
    background: linear-gradient(180deg, var(--skyline-soft) 0%, var(--skyline) 100%); }
  .card--back .skyline { top: 420px; height: 150px;
    background: linear-gradient(180deg, #dfe2f2 0%, #ffffff 100%); opacity: 0.9; }

  .contact { position: absolute; left: 108px; top: 548px; font-size: 14px; line-height: 19px;
    color: var(--ink); text-align: center; width: 240px; }

  .back-field { position: absolute; left: 0; right: 0; top: 385px; bottom: 0; background: var(--navy-deep); }
  .back-services { position: absolute; left: 0; right: 0; top: 587px; text-align: center; color: #fff;
    font-family: "Noto Serif JP", serif; font-size: 17px; line-height: 28px; letter-spacing: 1px; }

  .style-label { position: absolute; left: 540px; top: 128px; font-family: "Noto Serif JP", serif;
    font-size: 38px; color: var(--label); letter-spacing: 1px; }

  .formats { position: absolute; left: 62px; top: 945px; font-family: "Courier Prime", monospace;
    font-size: 25px; line-height: 36px; color: var(--label); white-space: pre; }
</style>
</head>
<body>
<main class="sheet">

  <section class="card card--front" aria-label="名刺 表面">
    <header class="band"><small>株式会社</small>青嶺建設</header>
    <div class="brand"><span class="brand__dot"></span>AOMINE</div>
    <p class="services">住宅設備・建設・建築工事 / 建設・建築工事業</p>
    <h1 class="name">大川誠</h1>
    <p class="role">代表取締役</p>
    <div class="skyline" role="img" aria-label="淡い紫色の街並みシルエット"></div>
    <address class="contact">
      Address:〒600-0000<br>
      架空市緑町123番地の4<br>
      TEL:(012)345-6789<br>
      FAX:(012)345-6790<br>
      E-Mail:info@aomine-kk.example
    </address>
  </section>

  <section class="card card--back" aria-label="名刺 裏面">
    <header class="band"><small>株式会社</small>青嶺建設</header>
    <div class="brand"><span class="brand__dot"></span>AOMINE</div>
    <div class="back-field"></div>
    <div class="skyline" role="img" aria-label="紺地に白い街並みシルエット"></div>
    <p class="back-services">住宅設備・建設・建築工事<br>建設・建築工事業</p>
  </section>

  <p class="style-label">Style №: C</p>

  <p class="formats">Adobe Photoshop.  .PSP
adobe illustrator .AI
Illustrator       .EPS
JPEG.             .JPG</p>

</main>
</body>
</html>
```